Badgerline Custom Woodcraft Website design

Need a small website to showcase my products and take orders

would also like payment options

We do custom wood work along with cnc work in wood plastic and soft metals

we are based in edmonton alberta canada
Updates

Industry/Entity Type

Work

Number of Pages Required

3 page

Requirements
Nice to have
• Interview for for a woodworking magazine
• http://timberquarterlyexample.com/issue-1-02-august-2016/member-spotlight
• I would also like to see metal working/branding iron info
• Also adding the picture of me from the above interview is a nice touch

```html
<!DOCTYPE html>
<html lang="en">
<head>
<meta charset="utf-8">
<title>Badgerline Custom Woodcraft</title>
<link href="https://fonts.googleapis.com/css2?family=Ubuntu:wght@400;500;700&family=Lato:wght@300;400;700&family=Roboto:wght@400;700&display=swap" rel="stylesheet">
<style>
:root{
  --white:#ffffff;
  --ink:#2b2b2b;
  --line:#c98a4a;
  --orange:#e07f22;
  --orange-dark:#b65c12;
  --star:#f2a11a;
  --navy:#0f2a63;
  --navy-soft:#1b3a7a;
  --wood-1:#e9a862;
  --wood-2:#d98b43;
  --wood-text:#4a2b10;
  --footer:#2a1a0e;
  --footer-bar:#1f130a;
  --footer-text:#f4e8dc;
  --blue-btn:#1f7fd0;
}
*{box-sizing:border-box;margin:0;padding:0}
html,body{width:1120px;height:1200px;overflow:hidden;background:var(--white)}
body{position:relative;font-family:"Ubuntu",sans-serif;color:var(--ink)}
.abs{position:absolute}

/* product cards */
.product-card{position:absolute;top:-30px;width:187px;height:143px;border:1px solid var(--line);border-top:none;background:var(--white);text-align:center}
.product-card .desc{font-family:"Lato",sans-serif;font-size:11px;line-height:14px;margin-top:30px;letter-spacing:.2px}
.product-card .rating{position:relative;height:20px;margin-top:4px}
.product-card .badge-new{position:absolute;left:9px;top:0;font-size:9px;color:var(--orange);border:1px solid var(--orange);border-radius:10px;padding:2px 6px}
.product-card .stars{display:inline-block;margin-top:2px}
.get-pricing{position:absolute;left:31px;top:92px;width:123px;height:37px;border-radius:3px;background:linear-gradient(#eea04a,var(--orange));border-bottom:4px solid var(--orange-dark);color:var(--white);font-weight:700;font-size:11.5px;line-height:33px;letter-spacing:.3px}

/* gallery */
.section-title{left:102px;top:189px;font-size:15px;font-weight:500;color:#333}
.tile{position:absolute}
.view-all{background:var(--navy-soft);color:var(--white);font-weight:500;font-size:13.5px;line-height:19px;display:flex;align-items:center;justify-content:center;text-align:center}
.view-all u{text-underline-offset:2px}

/* featured */
.band{left:0;top:713px;width:1120px;height:225px;background:var(--navy)}
.board{left:147px;top:656px;width:859px;height:118px;background:linear-gradient(180deg,var(--wood-1),var(--wood-2));box-shadow:0 2px 4px rgba(0,0,0,.35)}
.rivet{position:absolute;width:6px;height:6px;border-radius:50%;background:#555}
.feature-title{left:189px;top:678px;font-size:29px;color:var(--white);font-weight:400;letter-spacing:-.2px}
.feature-lead{left:191px;top:719px;font-size:14px;font-weight:500;color:var(--wood-text)}
.feature-lead a{color:var(--wood-text)}
.feature-date{left:502px;top:750px;font-size:8.5px;font-weight:700;color:var(--wood-text)}
.interview-photo{left:770px;top:592px;width:182px;height:140px;background:linear-gradient(135deg,#8a6a4a,#4a3a2c);border:4px solid #f1ece4;transform:rotate(-5deg);box-shadow:0 3px 8px rgba(0,0,0,.4)}
.interview-caption{left:790px;top:741px;font-size:13px;font-style:italic;color:var(--white);font-weight:500}

.quote{left:80px;top:803px;width:940px;font-family:"Lato",sans-serif;font-weight:300;font-size:19.5px;line-height:24px;color:var(--white)}
.quote-author{left:78px;top:868px;font-family:"Roboto",sans-serif;font-size:13px;color:var(--white)}
.dots{left:512px;top:895px;display:flex;gap:8px}
.dots span{width:12px;height:12px;border-radius:50%;border:1px solid var(--orange)}
.dots span.active{background:var(--orange-dark)}

/* footer */
.footer{left:0;top:938px;width:1120px;height:262px;background:var(--footer)}
.footer-bottom{left:0;top:1146px;width:1120px;height:54px;background:var(--footer-bar);border-top:1px solid #3a2718}
.brand{left:120px;top:1038px;display:flex;align-items:center;gap:8px;font-size:14px;font-weight:500;color:var(--orange)}
.brand .mark{width:14px;height:14px;border-radius:50%;background:var(--orange)}
.footer-heading{font-size:16px;font-weight:500;color:var(--white);letter-spacing:.3px}
.footer-links{list-style:none;font-size:11.5px;color:var(--footer-text);letter-spacing:.3px}
.footer-links li{height:24.5px}
.newsletter{left:746px;top:1026px;width:271px;height:32px;background:var(--white);border-radius:3px;overflow:hidden}
.newsletter .placeholder{position:absolute;left:12px;top:9px;font-size:12px;color:#999;letter-spacing:.5px}
.newsletter .submit{position:absolute;right:0;top:0;width:44px;height:32px;background:var(--blue-btn)}
.copyright{left:128px;top:1170px;font-family:"Lato",sans-serif;font-size:8.5px;color:var(--white)}
.pay-label{left:642px;top:1171px;font-family:"Lato",sans-serif;font-weight:700;font-size:8.5px;color:var(--white)}
.pay-card{position:absolute;top:1163px;width:40px;height:26px;border-radius:3px;background:#e9eef5;transform:rotate(-12deg)}
</style>
</head>
<body>

<svg width="0" height="0" style="position:absolute">
  <defs>
    <symbol id="star" viewBox="0 0 20 20"><path d="M10 1l2.6 6 6.4.5-4.9 4.2 1.5 6.3L10 14.6 4.4 18l1.5-6.3L1 7.5 7.4 7z" fill="#f2a11a"/></symbol>
  </defs>
</svg>

<!-- products -->
<div class="product-card" style="left:102px">
  <p class="desc">Short description here. liber<br>tempor cum soluta nobis</p>
  <div class="rating"><span class="badge-new">New</span><span class="stars"><svg width="70" height="13"><use href="#star" width="13" height="13"/><use href="#star" x="14" width="13" height="13"/><use href="#star" x="28" width="13" height="13"/><use href="#star" x="42" width="13" height="13"/><use href="#star" x="56" width="13" height="13"/></svg></span></div>
  <div class="get-pricing">Get Pricing</div>
</div>
<div class="product-card" style="left:344px">
  <p class="desc">Short description here. liber<br>tempor cum soluta nobis</p>
  <div class="rating"><span class="stars"><svg width="70" height="13"><use href="#star" width="13" height="13"/><use href="#star" x="14" width="13" height="13"/><use href="#star" x="28" width="13" height="13"/><use href="#star" x="42" width="13" height="13"/><use href="#star" x="56" width="13" height="13"/></svg></span></div>
  <div class="get-pricing">Get Pricing</div>
</div>
<div class="product-card" style="left:586px">
  <p class="desc">Short description here. liber<br>tempor cum soluta nobis</p>
  <div class="rating"><span class="stars"><svg width="70" height="13"><use href="#star" width="13" height="13"/><use href="#star" x="14" width="13" height="13"/><use href="#star" x="28" width="13" height="13"/><use href="#star" x="42" width="13" height="13"/><use href="#star" x="56" width="13" height="13"/></svg></span></div>
  <div class="get-pricing">Get Pricing</div>
</div>
<div class="product-card" style="left:828px">
  <p class="desc">Short description here. liber<br>tempor cum soluta nobis</p>
  <div class="rating"><span class="badge-new">New</span><span class="stars"><svg width="70" height="13"><use href="#star" width="13" height="13"/><use href="#star" x="14" width="13" height="13"/><use href="#star" x="28" width="13" height="13"/><use href="#star" x="42" width="13" height="13"/><use href="#star" x="56" width="13" height="13"/></svg></span></div>
  <div class="get-pricing">Get Pricing</div>
</div>

<!-- gallery -->
<h2 class="abs section-title">Recent WoodWorks Projects</h2>
<div class="tile" role="img" aria-label="Cedar wood chairs with carved nameplates" style="left:48px;top:221px;width:283px;height:144px;background:linear-gradient(135deg,#c99a6a,#a9764a)"></div>
<div class="tile" role="img" aria-label="Engraved metal plate with a farmhouse scene" style="left:333px;top:221px;width:284px;height:144px;background:linear-gradient(135deg,#9b9590,#5e5a56)"></div>
<div class="tile" role="img" aria-label="Carved walnut panel beneath a dartboard" style="left:619px;top:221px;width:284px;height:144px;background:linear-gradient(135deg,#9a8a6e,#6a4a2e)"></div>
<div class="tile" role="img" aria-label="Engraved pine sign for the workshop" style="left:905px;top:221px;width:166px;height:144px;background:linear-gradient(180deg,#e7c99a,#cfa36a)"></div>

<div class="tile" role="img" aria-label="Carved wooden owl sculpture" style="left:48px;top:366px;width:183px;height:144px;background:linear-gradient(135deg,#7a6040,#4a3a26)"></div>
<div class="tile" role="img" aria-label="Round carved wooden union seal" style="left:233px;top:366px;width:184px;height:144px;background:linear-gradient(135deg,#8a6a50,#5a3c28)"></div>
<div class="tile" role="img" aria-label="CNC machine engraving a black disc" style="left:419px;top:366px;width:184px;height:144px;background:linear-gradient(135deg,#6a6a6a,#1e1e1e)"></div>
<div class="tile" role="img" aria-label="Engraved pine sign close-up" style="left:605px;top:366px;width:183px;height:144px;background:linear-gradient(180deg,#e7c99a,#cfa36a)"></div>
<div class="tile" role="img" aria-label="Carved eagle head in red wood" style="left:790px;top:366px;width:184px;height:144px;background:linear-gradient(135deg,#d0743a,#9a3a1c)"></div>
<div class="tile view-all" style="left:976px;top:366px;width:95px;height:144px"><span>Veiw<br>All<br><u>Designs</u></span></div>

<!-- featured -->
<div class="abs band"></div>
<div class="abs board" role="img" aria-label="Wooden plank banner">
  <span class="rivet" style="left:20px;top:18px"></span>
  <span class="rivet" style="left:20px;top:96px"></span>
  <span class="rivet" style="left:836px;top:16px"></span>
  <span class="rivet" style="left:836px;top:96px"></span>
</div>
<p class="abs feature-title">Featured In Timber Quarterly Magazine</p>
<p class="abs feature-lead">Lorem ipsum dolor sit amet and some description here. <a href="http://timberquarterlyexample.com/issue-1-02-august-2016/member-spotlight">Read More...</a></p>
<p class="abs feature-date">August 31, 2016, Ridge Rd, Maple Falls, Alberta</p>
<div class="abs interview-photo" role="img" aria-label="Photo of the craftsman in his stable workshop"></div>
<p class="abs interview-caption">Interview with Dale Morrow</p>

<p class="abs quote">&ldquo;Badgerline WoodWorks was very excellent in dcrafting our liber tempor cum soluta nobis eleifend option congue nihil imperdiet doming id quod mazim placerat facer possim assum.</p>
<p class="abs quote-author"><b>Henrietta Bloom,</b> 12 Birch Lane, Location, Alberta</p>
<div class="abs dots"><span></span><span class="active"></span><span></span><span></span><span></span></div>

<!-- footer -->
<div class="abs footer"></div>
<div class="abs brand"><span class="mark"></span>Badgerline Custom Woodcraft</div>

<h3 class="abs footer-heading" style="left:360px;top:987px">QUICK LINKS</h3>
<ul class="abs footer-links" style="left:361px;top:1027px">
  <li>About Badgerline</li><li>Contact Us</li><li>Support</li><li>Reviews</li>
</ul>
<h3 class="abs footer-heading" style="left:554px;top:987px">CUSTOMERS</h3>
<ul class="abs footer-links" style="left:555px;top:1027px">
  <li>FAQ</li><li>Help</li><li>Pricing</li><li>Shipping &amp; Delivery</li>
</ul>
<h3 class="abs footer-heading" style="left:746px;top:987px">SIGN UP FOR OUR NEWS LETTER!</h3>
<div class="abs newsletter">
  <span class="placeholder">ENTER YOUR EMAIL ADDRESS</span>
  <span class="submit"><svg width="44" height="32" viewBox="0 0 44 32"><path d="M15 16h13M23 10l6 6-6 6" stroke="#fff" stroke-width="3" fill="none" stroke-linecap="round" stroke-linejoin="round"/></svg></span>
</div>

<div class="abs footer-bottom"></div>
<p class="abs copyright">COPYRIGHT &copy; 2016 - BADGERLINE. CUSTOM WOODCRAFT &nbsp;ALL RIGHTS RESERVED.</p>
<p class="abs pay-label">AVAILABLE PAYMENT OPTIONS:</p>
<span class="pay-card" style="left:786px"></span>
<span class="pay-card" style="left:834px"></span>
<span class="pay-card" style="left:882px"></span>
<span class="pay-card" style="left:930px"></span>
<span class="pay-card" style="left:976px"></span>

</body>
</html>
```